Sound Crate Hire (business card/packet folder/stationary)

Designers:
The address will not longer be included in any of these designs. Thanks!

Attention designers,
It was brought to my attention that my brief was too broad and VERY confusing :/. I truly apologize.

This is what I need:
*Front and back business cards.
*A packet folder (front and back) (The size big enough to hold the 8x11 sheets)
I really don't know he size.

*Letter head

I needs to be professional, elegant, and it needs to stand out. Corporate like.

Colors:
Deep Red, Black, Deep blue . Also, follow color scheme of current logo but get creative.

Company: Sound Crate Hire Prairie
Phone: 918.555.0142
Email: Bookings@SoundCrateHirePrairie.example
Web: www.SoundCrateHirePrairie.example (under construction)
Address: 4826 W. 9th Court, Tulsa, OK 74100
Logo: Provided

Project Deadline Extended
Reason: Due to my poor explanation and description of the project, I'm extending the due date of this project.

Target Market(s)

This folder will have my information as a business and it will serve as a marketing material. The audience range age is 18-43.

Industry/Entity Type

Business

Requirements
Must have
• Follow the color scheme provide in the logo.

```html
<!DOCTYPE html>
<html lang="en">
<head>
<meta charset="utf-8">
<title>Sound Crate Hire Prairie — Stationery Set</title>
<link rel="stylesheet" href="https://fonts.googleapis.com/css2?family=Roboto:wght@300;400;700&display=swap">
<style>
  :root{
    --bg:#c4c4c4;
    --ink:#0c0c0c;
    --ink-line:#2a2a2a;
    --paper:#ffffff;
    --orange:#f7941d;
    --red:#e2362b;
    --muted:#9a9a9a;
    --eq:linear-gradient(90deg,#f6c445 0%,#f7941d 14%,#e2362b 28%,#9e2a3a 42%,#c2413a 52%,#f08a3c 62%,#6fc1c9 74%,#3aa5c7 86%,#2a6fa8 100%);
  }
  *{box-sizing:border-box;margin:0;padding:0}
  html,body{width:1200px;height:1000px;overflow:hidden}
  body{background:var(--bg);font-family:"Roboto",Arial,sans-serif;position:relative;color:var(--paper)}
  .piece{position:absolute;overflow:hidden}

  .brand{display:flex;align-items:center;gap:6px;white-space:nowrap}
  .brand-dot{width:8px;height:8px;border-radius:50%;background:var(--orange);flex:none}
  .brand-name{font-weight:700;color:var(--orange);letter-spacing:.04em;text-transform:uppercase}

  .eq-strip{position:absolute;left:0;right:0;bottom:0;background:var(--eq)}

  .contact{list-style:none;font-size:7px;line-height:1.6}
  .contact li{display:flex;align-items:center;gap:5px;white-space:nowrap}
  .contact svg{width:8px;height:8px;flex:none}
  .bullet{width:5px;height:5px;background:var(--red);flex:none}

  /* folder */
  .folder-panel{background:linear-gradient(160deg,#1e1e1e 0%,var(--ink) 60%);}
  .folder-front .corner-band{position:absolute;top:0;right:0;width:48px;height:150px;background:linear-gradient(180deg,var(--orange),var(--red))}
  .folder-front .brand{position:absolute;left:22px;bottom:30px}
  .folder-front .brand-name{font-size:11px}
  .folder-back .contact{position:absolute;right:20px;bottom:26px;color:#bbb;font-size:6px}
  .folder-inside{display:flex}
  .folder-inside .folder-panel{position:relative;width:280px;height:360px}
  .folder-inside .folder-panel + .folder-panel{border-left:1px solid var(--ink-line)}
  .pocket{position:absolute;left:0;right:0;bottom:0;height:110px;background:linear-gradient(180deg,#222,#111);clip-path:polygon(0 22%,100% 0,100% 100%,0 100%)}
  .pocket .brand{position:absolute;right:16px;bottom:18px}
  .pocket .brand-name{font-size:9px}
  .insert-sheet{position:absolute;left:70px;top:40px;width:170px;height:230px;background:var(--paper)}
  .insert-sheet .sheet-head{height:16px;background:var(--ink)}

  /* letterhead */
  .letterhead{background:var(--paper)}
  .lh-head{height:70px;background:var(--ink);display:flex;justify-content:space-between;align-items:center;padding:0 18px}
  .lh-head .brand-name{font-size:12px}
  .lh-head .contact{color:#ddd}
  .letterhead .eq-strip{height:14px}

  /* envelope */
  .envelope{background:var(--paper)}
  .env-head{height:80px;background:var(--ink);display:flex;align-items:center;padding:0 26px}
  .env-head .brand-name{font-size:16px}
  .envelope .contact{position:absolute;left:26px;top:100px;color:#444;font-size:9px}
  .envelope .bullet{width:7px;height:7px}
  .envelope .eq-strip{height:22px}

  /* business cards */
  .card{background:linear-gradient(160deg,#1d1d1d,var(--ink))}
  .card-front .side-band{position:absolute;left:0;top:0;bottom:0;width:80px;background:linear-gradient(160deg,#f9c23c,var(--orange) 45%,var(--red))}
  .card-person{position:absolute;right:20px;top:18px;text-align:right}
  .card-person .name{color:var(--orange);font-size:15px;font-weight:400}
  .card-person .role{color:var(--muted);font-size:8px;font-weight:300}
  .card-front .contact{position:absolute;left:98px;top:86px;color:#eee;font-size:8.5px}
  .card-front .contact svg{width:9px;height:9px}
  .card-front .eq-strip{left:80px;height:10px}
  .card-back{display:flex;align-items:center;justify-content:center}
  .card-back .brand-name{font-size:17px}
  .card-back .brand-dot{width:12px;height:12px}
</style>
</head>
<body>

<svg width="0" height="0" style="position:absolute" aria-hidden="true">
  <defs>
    <symbol id="i-fax" viewBox="0 0 10 10"><rect width="10" height="10" rx="1.5" fill="#fff"/><rect x="2.5" y="2" width="5" height="6" fill="#111"/></symbol>
    <symbol id="i-phone" viewBox="0 0 10 10"><rect width="10" height="10" rx="1.5" fill="#fff"/><path d="M3 2.2l1.2 1.6-.7.8c.5 1 1.2 1.7 2.1 2.1l.8-.7L8 7.2 7.2 8.3C4.6 7.9 2.3 5.6 1.9 3z" fill="#111"/></symbol>
    <symbol id="i-mail" viewBox="0 0 10 10"><rect width="10" height="10" rx="1.5" fill="#fff"/><rect x="2" y="3" width="6" height="4" fill="none" stroke="#111" stroke-width=".8"/><path d="M2 3l3 2.3L8 3" fill="none" stroke="#111" stroke-width=".8"/></symbol>
    <symbol id="i-web" viewBox="0 0 10 10"><rect width="10" height="10" rx="1.5" fill="#fff"/><circle cx="5" cy="5" r="2.8" fill="none" stroke="#111" stroke-width=".8"/><path d="M2.2 5h5.6M5 2.2v5.6" stroke="#111" stroke-width=".6"/></symbol>
  </defs>
</svg>

<!-- Folder front cover -->
<section class="piece folder-panel folder-front" style="left:30px;top:30px;width:260px;height:360px">
  <div class="corner-band"></div>
  <div class="brand"><span class="brand-dot"></span><span class="brand-name">Sound Crate Hire Prairie</span></div>
</section>

<!-- Folder back cover -->
<section class="piece folder-panel folder-back" style="left:310px;top:30px;width:260px;height:360px">
  <ul class="contact">
    <li><span class="bullet"></span>918.555.0142</li>
    <li><span class="bullet"></span>Bookings@SoundCrateHirePrairie.example</li>
    <li><span class="bullet"></span>www.SoundCrateHirePrairie.example</li>
  </ul>
</section>

<!-- Folder inside spread -->
<section class="piece folder-inside" style="left:590px;top:30px;width:560px;height:360px">
  <div class="folder-panel">
    <div class="pocket">
      <div class="brand"><span class="brand-dot"></span><span class="brand-name">Sound Crate Hire Prairie</span></div>
    </div>
  </div>
  <div class="folder-panel">
    <div class="insert-sheet"><div class="sheet-head"></div></div>
    <div class="pocket">
      <div class="brand"><span class="brand-dot"></span><span class="brand-name">Sound Crate Hire Prairie</span></div>
    </div>
  </div>
</section>

<!-- Letterhead -->
<section class="piece letterhead" style="left:30px;top:420px;width:410px;height:530px">
  <header class="lh-head">
    <div class="brand"><span class="brand-dot"></span><span class="brand-name">Sound Crate Hire Prairie</span></div>
    <ul class="contact">
      <li><span class="bullet"></span>918.555.0142</li>
      <li><span class="bullet"></span>Bookings@SoundCrateHirePrairie.example</li>
      <li><span class="bullet"></span>www.SoundCrateHirePrairie.example</li>
    </ul>
  </header>
  <div class="eq-strip" role="img" aria-label="Equalizer bar pattern in warm reds, oranges and blues"></div>
</section>

<!-- Envelope -->
<section class="piece envelope" style="left:470px;top:420px;width:700px;height:300px">
  <header class="env-head">
    <div class="brand"><span class="brand-dot"></span><span class="brand-name">Sound Crate Hire Prairie</span></div>
  </header>
  <ul class="contact">
    <li><span class="bullet"></span>918.555.0142</li>
    <li><span class="bullet"></span>Bookings@SoundCrateHirePrairie.example</li>
    <li><span class="bullet"></span>www.SoundCrateHirePrairie.example</li>
  </ul>
  <div class="eq-strip" role="img" aria-label="Equalizer bar pattern in warm reds, oranges and blues"></div>
</section>

<!-- Business card front -->
<section class="piece card card-front" style="left:470px;top:750px;width:330px;height:200px">
  <div class="side-band"></div>
  <div class="card-person">
    <p class="name">Dana Whitfield</p>
    <p class="role">Founder</p>
  </div>
  <ul class="contact">
    <li><svg><use href="#i-fax"/></svg>000.000.000</li>
    <li><svg><use href="#i-phone"/></svg>918.555.0142</li>
    <li><svg><use href="#i-mail"/></svg>Bookings@SoundCrateHirePrairie.example</li>
    <li><svg><use href="#i-web"/></svg>www.SoundCrateHirePrairie.example</li>
  </ul>
  <div class="eq-strip" role="img" aria-label="Equalizer bar pattern in warm reds, oranges and blues"></div>
</section>

<!-- Business card back -->
<section class="piece card card-back" style="left:840px;top:750px;width:330px;height:200px">
  <div class="brand"><span class="brand-dot"></span><span class="brand-name">Sound Crate Hire Prairie</span></div>
</section>

</body>
</html>
```